WordPress Coding + Design - Website designed to maximise leads required

Please see the velmora brief.doc file

it is VERY important that this website be DESIGNED with MOBILE + TABLET BOOTSTRAP in mind.

The design has to look amazing on mobile and tablet.

Reason: Designer failed to meet expectations and wasted my time

1 page

```html
<!DOCTYPE html>
<html lang="en">
<head>
<meta charset="utf-8">
<title>Velmora College Advisors</title>
<link rel="stylesheet" href="https://fonts.googleapis.com/css2?family=Roboto:ital,wght@0,300;0,400;0,500;0,700;1,400&family=Roboto+Condensed:wght@400;700&family=Open+Sans:ital,wght@0,400;0,600;1,400&display=swap">
<style>
:root{
  --gold:#d9a02b;
  --gold-dark:#b9861f;
  --blue:#233f93;
  --blue-dark:#1a2f6e;
  --ink:#333;
  --muted:#777;
  --light:#f4f4f4;
  --band:#e8e8e8;
  --white:#fff;
  --cream:#f3ead6;
  --green:#6b9a3a;
  --orange:#e79a1a;
  --sky:#3f8fd2;
}
*{box-sizing:border-box;margin:0;padding:0}
html,body{width:1200px;height:3235px;overflow:hidden}
body{font-family:"Open Sans",Arial,sans-serif;color:var(--ink);background:var(--white);font-size:14px;line-height:1.55}
.wrap{width:930px;margin:0 auto;position:relative}
section,header,footer{position:relative;width:1200px}

/* top bar */
.topbar{height:29px;background:var(--light);border-bottom:1px solid #ddd;font-size:12px}
.topbar .wrap{display:flex;justify-content:space-between;align-items:center;height:29px}
.lang,.account{display:flex;gap:14px;align-items:center}
.lang span,.account span{display:flex;align-items:center;gap:5px}
.flag{width:14px;height:9px;background:#c33;display:inline-block}
.flag.alt{background:#2a7a3b}
.acc-ico{width:10px;height:10px;background:#666;border-radius:2px;display:inline-block}

/* brand */
.brand{height:91px;display:flex;justify-content:center;align-items:center}
.brand-lockup{display:flex;align-items:center;gap:12px}
.brand-dot{width:56px;height:56px;border-radius:50%;background:var(--blue)}
.brand-name{font-family:"Roboto",sans-serif;font-weight:700;font-size:30px;color:var(--blue);line-height:1;letter-spacing:.5px}
.brand-name small{display:block;font-size:13px;letter-spacing:2.3px;margin-top:4px}

/* nav */
.mainnav{height:42px;background:var(--gold)}
.mainnav ul{list-style:none;display:flex;height:42px}
.mainnav a{display:block;padding:0 16px;line-height:42px;color:var(--white);text-decoration:none;font-family:"Roboto",sans-serif;font-size:15px;font-weight:500}
.mainnav li.active a{background:var(--blue)}

/* hero */
.hero{height:436px;overflow:hidden}
.hero-photo{position:absolute;inset:0;background:linear-gradient(100deg,#5b6673 0%,#7e8a96 35%,#c9cdd2 60%,#e6e2dc 100%)}
.hero-text{position:absolute;left:135px;top:120px;color:var(--white);font-family:"Roboto",sans-serif}
.hero-text .lead{font-size:23px;font-weight:500}
.hero-text h1{font-family:"Roboto Condensed",sans-serif;font-size:104px;font-weight:700;line-height:.95;margin-top:6px}
.hero-text .sub{font-family:"Roboto Condensed",sans-serif;font-size:44px;font-weight:700;line-height:1.1}
.hero-text .tag{font-size:22px;margin-top:4px}

/* headings */
.sec-title{text-align:center;font-family:"Roboto",sans-serif;color:var(--blue);font-weight:400;letter-spacing:.5px}
.sec-kicker{text-align:center;font-family:"Roboto",sans-serif;color:var(--gold);font-size:26px;letter-spacing:.5px}

/* welcome */
.welcome{height:470px;background:var(--light)}
.welcome .sec-kicker{padding-top:38px}
.welcome .sec-title{font-size:34px;line-height:1.2}
.welcome-body{display:flex;justify-content:space-between;margin-top:42px}
.welcome-copy{width:455px;font-size:14px;color:#444}
.welcome-copy p{margin-bottom:16px}
.read-more{color:var(--blue);text-decoration:underline;font-size:14px}
.video{width:350px;height:228px;background:linear-gradient(160deg,#4a4a4a,#7b2f4c 55%,#2a2a2a);margin-right:55px;border:1px solid #ccc}
.arrow{position:absolute;width:22px;height:22px;border:1px solid #bbb;background:var(--white);display:flex;align-items:center;justify-content:center}
.arrow svg{width:8px;height:10px}

/* services */
.services{height:478px;background:var(--white)}
.services .sec-title{font-size:32px;padding-top:40px}
.services-intro{text-align:center;font-size:15px;color:#555;width:760px;margin:18px auto 0}
.services-intro a{color:var(--blue);text-decoration:underline}
.service-row{display:flex;justify-content:center;margin-top:30px;height:290px;background:linear-gradient(var(--band),var(--band)) center 40px/100% 210px no-repeat}
.service-card{width:228px;height:240px;background:var(--cream);margin:20px 2px 0;box-shadow:0 3px 8px rgba(0,0,0,.25);padding:30px 28px;font-family:"Roboto",sans-serif}
.service-card:first-child{border-left:8px solid #c9b58c}
.service-card:last-child{border-right:8px solid #c9b58c}
.service-icon{width:64px;height:64px;border-radius:50%;margin-bottom:16px}
.service-card h3{font-size:17px;font-weight:700;color:#333}
.service-card p{font-size:11px;color:#888;line-height:1.4;margin-top:6px}

/* partners */
.partners{height:211px;background:var(--band)}
.partners .sec-title{font-size:32px;padding-top:26px}
.logo-row{display:flex;justify-content:space-between;align-items:center;width:930px;margin:38px auto 0}
.logo-chip{height:46px;background:#bfc3cc;border-radius:4px}

/* testimonials */
.testimonials{height:443px;background:linear-gradient(90deg,#1f2b24,#37503f 50%,#243128);color:var(--white);overflow:hidden}
.testimonials h2{text-align:center;font-family:"Roboto",sans-serif;font-weight:700;font-size:34px;padding-top:22px}
.testimonials .caption{text-align:center;font-style:italic;font-size:13px}
.student-photo{position:absolute;left:210px;top:110px;width:270px;height:333px;background:linear-gradient(180deg,#8a6d54,#c8b39c 45%,#d97a6a 75%,#b8b8c4)}
.quote-box{position:absolute;left:560px;top:118px;width:445px;height:180px;background:var(--white);color:#666;padding:26px 30px 20px 70px;font-size:13px;font-style:italic}
.quote-mark{position:absolute;left:18px;top:52px;width:36px;height:36px;border-radius:50%;background:#2b2b2b}
.quote-box .who{font-family:"Roboto",sans-serif;font-style:italic;color:var(--gold);font-weight:700;font-size:17px;margin-top:6px}
.avatars{position:absolute;left:590px;top:315px;display:flex;gap:26px}
.avatar{text-align:center;width:62px}
.avatar-img{width:50px;height:50px;border-radius:50%;background:#c9b7a6;border:2px solid var(--white);margin:0 auto 4px}
.avatar span{display:block;font-size:10px;line-height:1.3;white-space:nowrap}
.avatar small{display:block;font-size:9px;color:#b9c4bb}

/* media */
.media{height:178px;background:var(--band)}
.media .logo-row{margin-top:0;padding-top:62px}

/* contact */
.contact{height:511px;background:var(--white)}
.contact .sec-title{font-size:32px;padding-top:28px}
.contact-intro{text-align:center;font-size:15px;color:#555;width:600px;margin:6px auto 0;line-height:1.4}
.contact-body{display:flex;justify-content:space-between;margin-top:64px}
.contact-info{width:400px;padding-top:6px}
.info-row{display:flex;gap:26px;align-items:flex-start;margin-bottom:38px;font-size:15px;color:#555}
.info-row .ico{flex:none;width:38px;height:38px;border-radius:50%;border:2px solid var(--blue);display:flex;align-items:center;justify-content:center}
.info-row .ico svg{width:18px;height:18px;fill:var(--blue)}
.info-row p{width:280px;line-height:1.4}
.contact-form{width:470px}
.field{height:38px;border:1px solid #ccc;margin-bottom:14px;display:flex;align-items:center;padding-left:14px;color:#999;font-size:13px;gap:14px}
.field i{width:12px;height:12px;background:#bbb;border-radius:2px;display:inline-block}
.field.message{height:110px}
.submit{display:block;margin-left:auto;margin-top:26px;width:150px;height:46px;background:var(--blue);color:var(--white);border:0;font-family:"Roboto",sans-serif;font-weight:500;font-size:16px}

/* map */
.map{height:297px;background:linear-gradient(135deg,#e3e0d8,#cfd6d9 50%,#e8e4da)}
.map-pin{position:absolute;left:545px;top:85px;width:28px;height:40px}

/* footer */
.site-footer{height:49px;background:var(--gold)}
.site-footer .wrap{display:flex;justify-content:space-between;align-items:center;height:49px;color:var(--white);font-size:14px}
.social{display:flex;gap:12px}
.social span{width:30px;height:30px;border-radius:50%;border:2px solid var(--white)}
</style>
</head>
<body>

<header class="topbar">
  <div class="wrap">
    <div class="lang"><span><i class="flag"></i>English</span><span><i class="flag alt"></i>Arabic</span></div>
    <div class="account"><span><i class="acc-ico"></i>Sign In</span><span><i class="acc-ico"></i>Register</span></div>
  </div>
</header>

<header class="brand">
  <div class="brand-lockup">
    <span class="brand-dot"></span>
    <div class="brand-name">VELMORA<small>COLLEGE ADVISORS</small></div>
  </div>
</header>

<nav class="mainnav">
  <ul class="wrap">
    <li class="active"><a href="#">HOME</a></li>
    <li><a href="#">ABOUT</a></li>
    <li><a href="#">STUDENTS</a></li>
    <li><a href="#">OUR TEAM</a></li>
    <li><a href="#">SERVICES</a></li>
    <li><a href="#">MEDIA</a></li>
    <li><a href="#">FAQ</a></li>
    <li><a href="#">LINKS</a></li>
    <li><a href="#">EVENTS</a></li>
    <li><a href="#">LOCATION</a></li>
  </ul>
</nav>

<section class="hero">
  <div class="hero-photo" role="img" aria-label="Smiling student holding notebooks outside a campus building"></div>
  <div class="hero-text">
    <p class="lead">Want to Fulfill your dream of studying in the USA?</p>
    <h1>WE GUIDE</h1>
    <p class="sub">AND EMPOWER STUDENTS</p>
    <p class="tag">We are your US University specialists in the GCC</p>
  </div>
</section>

<section class="welcome">
  <p class="sec-kicker">WELCOME TO</p>
  <h2 class="sec-title">VELMORA COLLEGE ADVISORS</h2>
  <div class="wrap welcome-body">
    <div class="welcome-copy">
      <p>When you engage us, you have access to an entire team of American university professionals with relevant firsthand admissions experience, education, and knowledge. Velmora will help you with the key stages of preparation, research, and application to US universities and guide you in your critical first steps into the future.</p>
      <p>Our team has comprehensive experience in meeting application deadlines, evaluating transcripts, advising on letters of recommendation, essay brainstorming and revision, completing the Shared College Application, supervising student visa application procedures, and exploring Financial Aid options.</p>
      <a class="read-more" href="#">Read More</a>
    </div>
    <div class="video" role="img" aria-label="Video player: why study in the United States"></div>
    <span class="arrow" style="left:478px;top:90px"><svg viewBox="0 0 8 10"><path d="M7 0L1 5l6 5" fill="none" stroke="#999" stroke-width="1.5"/></svg></span>
    <span class="arrow" style="right:5px;top:90px"><svg viewBox="0 0 8 10"><path d="M1 0l6 5-6 5" fill="none" stroke="#999" stroke-width="1.5"/></svg></span>
  </div>
</section>

<section class="services">
  <h2 class="sec-title">VELMORA SERVICES</h2>
  <p class="services-intro">Applying to US universities is a holistic process, which typically involves the submission of a personal statement, supplemental essays, standardized test scores, academic transcripts... <a href="#">Read More</a></p>
  <div class="service-row">
    <div class="service-card"><div class="service-icon" style="background:var(--green)"></div><h3>Sports Package</h3><p>Lorem Ipsum is simply dummy text of the printing and typesetting industry.</p></div>
    <div class="service-card"><div class="service-icon" style="background:var(--orange)"></div><h3>Crimson Package</h3><p>Lorem Ipsum is simply dummy text of the printing and typesetting industry.</p></div>
    <div class="service-card"><div class="service-icon" style="background:var(--orange)"></div><h3>Ivy Package</h3><p>Lorem Ipsum is simply dummy text of the printing and typesetting industry.</p></div>
    <div class="service-card"><div class="service-icon" style="background:var(--sky)"></div><h3>MS/MA</h3><p>Lorem Ipsum is simply dummy text of the printing and typesetting industry.</p></div>
  </div>
  <span class="arrow" style="left:122px;top:306px"><svg viewBox="0 0 8 10"><path d="M7 0L1 5l6 5" fill="none" stroke="#999" stroke-width="1.5"/></svg></span>
  <span class="arrow" style="right:122px;top:306px"><svg viewBox="0 0 8 10"><path d="M1 0l6 5-6 5" fill="none" stroke="#999" stroke-width="1.5"/></svg></span>
</section>

<section class="partners">
  <h2 class="sec-title">OUR PARTNERS</h2>
  <div class="logo-row">
    <span class="arrow" style="position:static"><svg viewBox="0 0 8 10"><path d="M7 0L1 5l6 5" fill="none" stroke="#999" stroke-width="1.5"/></svg></span>
    <span class="logo-chip" style="width:80px"></span>
    <span class="logo-chip" style="width:52px;border-radius:50%"></span>
    <span class="logo-chip" style="width:60px"></span>
    <span class="logo-chip" style="width:80px"></span>
    <span class="logo-chip" style="width:70px"></span>
    <span class="logo-chip" style="width:100px"></span>
    <span class="arrow" style="position:static"><svg viewBox="0 0 8 10"><path d="M1 0l6 5-6 5" fill="none" stroke="#999" stroke-width="1.5"/></svg></span>
  </div>
</section>

<section class="testimonials">
  <h2>Read Our Testimonials</h2>
  <p class="caption">What Students say</p>
  <div class="student-photo" role="img" aria-label="Student sitting cross-legged with a laptop"></div>
  <div class="quote-box">
    <span class="quote-mark"></span>
    <p>Nunc ullamcorper massa eu magna varius commodo. Praesent nec enim eu quam suscipit tincidunt at sed tortor. Quisque quis massa faucibus leo egestas rhoncus. Cras pretium rhoncus urna nec accumsan. Proin vehicula ante non pulvinar dignissim.</p>
    <p class="who">Lena Marrow</p>
  </div>
  <div class="avatars">
    <div class="avatar"><div class="avatar-img" role="img" aria-label="Student portrait"></div><span>Lena Marrow</span><small>Student</small></div>
    <div class="avatar"><div class="avatar-img" role="img" aria-label="Student portrait"></div><span>Mira Solen</span><small>Student</small></div>
    <div class="avatar"><div class="avatar-img" role="img" aria-label="Student portrait"></div><span>Owen Hale</span><small>Student</small></div>
    <div class="avatar"><div class="avatar-img" role="img" aria-label="Student portrait"></div><span>Tessa Lind</span><small>Student</small></div>
    <div class="avatar"><div class="avatar-img" role="img" aria-label="Student portrait"></div><span>Arlo Penn</span><small>Student</small></div>
  </div>
</section>

<section class="media">
  <div class="logo-row">
    <span class="arrow" style="position:static"><svg viewBox="0 0 8 10"><path d="M7 0L1 5l6 5" fill="none" stroke="#999" stroke-width="1.5"/></svg></span>
    <span class="logo-chip" style="width:70px;height:60px;border-radius:50%"></span>
    <span class="logo-chip" style="width:130px;height:30px"></span>
    <span class="logo-chip" style="width:130px;height:70px"></span>
    <span class="logo-chip" style="width:120px;height:50px"></span>
    <span class="logo-chip" style="width:140px;height:40px"></span>
    <span class="arrow" style="position:static"><svg viewBox="0 0 8 10"><path d="M1 0l6 5-6 5" fill="none" stroke="#999" stroke-width="1.5"/></svg></span>
  </div>
</section>

<section class="contact">
  <h2 class="sec-title">CONTACT US</h2>
  <p class="contact-intro">Lorem ipsum dolor sit amet, consectetur adipisicing elit, sed do eiusmod tempor incididunt ut labore et dolore magna aliqua. Ut enim ad minim</p>
  <div class="wrap contact-body">
    <div class="contact-info">
      <div class="info-row"><span class="ico"><svg viewBox="0 0 24 24"><path d="M12 2a7 7 0 0 0-7 7c0 5 7 13 7 13s7-8 7-13a7 7 0 0 0-7-7zm0 9.5A2.5 2.5 0 1 1 12 6.5a2.5 2.5 0 0 1 0 5z"/></svg></span><p>Our office is located in the Palmera Atrium Building on Harbor Crest Road. Parking is available on the street or at the on-site parking lot at the rate</p></div>
      <div class="info-row"><span class="ico"><svg viewBox="0 0 24 24"><path d="M6.6 10.8a15 15 0 0 0 6.6 6.6l2.2-2.2c.3-.3.7-.4 1-.2 1.1.4 2.3.6 3.6.6.6 0 1 .4 1 1V20c0 .6-.4 1-1 1A17 17 0 0 1 3 4c0-.6.4-1 1-1h3.5c.6 0 1 .4 1 1 0 1.3.2 2.5.6 3.6.1.3 0 .7-.2 1z"/></svg></span><p>+971 4 550 2140</p></div>
      <div class="info-row"><span class="ico"><svg viewBox="0 0 24 24"><path d="M3 5h18v14H3zm2 2v.5l7 4.5 7-4.5V7zm0 2.8V17h14V9.8l-7 4.5z"/></svg></span><p>velmoracollage@info.com</p></div>
    </div>
    <form class="contact-form">
      <div class="field"><i></i>name</div>
      <div class="field"><i></i>email</div>
      <div class="field message"></div>
      <button class="submit" type="button">SUBMIT</button>
    </form>
  </div>
</section>

<section class="map" role="img" aria-label="Street map showing the office location">
  <svg class="map-pin" viewBox="0 0 28 40"><path d="M14 0a14 14 0 0 0-14 14c0 10 14 26 14 26s14-16 14-26A14 14 0 0 0 14 0z" fill="#222"/><circle cx="14" cy="14" r="5" fill="#fff"/></svg>
</section>

<footer class="site-footer">
  <div class="wrap">
    <p>Copy Right 2015 @ Velmora College Advisors</p>
    <div class="social"><span></span><span></span><span></span><span></span></div>
  </div>
</footer>

</body>
</html>
```